Tessa Moor Catalog to submit to vendors

We need a catalog made with all of the products in our shop for sales purposes. Our Website is www.tessamoorandfriends.example
Almost all of our products are listed on the website. If you can not take the pictures from the site I can upload them. The descriptions are listed as well. There are three additional products that I will upload. This Catalog will be mailed to stores and should include MSRP Prices.
Updates

Hello There-We are looking for a sales catalog to send to stores in our area. We would like to include MSRP and the end we can add wholesale pricing with minimum orders. Our website is www.tessamoorandfriends.example. There are a few products that haven't been added to the website yet. Where can I upload them and send descriptions?Thank you,Colette Added Thursday, January 21, 2016

Target Market(s)

boutiques and gift shops

Industry/Entity Type

Shop

Font styles to use
Serif
Other font styles liked:
• Noteworthy

Colors
e34297
a64599
6b449b
0255a3

Requirements
Must have
• Color! I would like to organize the catalog by sections. Our premade section and our DIY kits. Maybe we should include Gift sets and put the baskets and gift boxes in one section

```html
<!DOCTYPE html>
<html lang="en">
<head>
<meta charset="utf-8">
<title>Tessa Moor Catalog – Bodywash Spread</title>
<link rel="stylesheet" href="https://fonts.googleapis.com/css2?family=Josefin+Sans:wght@300;400;600&display=swap">
<style>
  :root{
    --pink:#e34297;
    --orchid:#a64599;
    --violet:#6b449b;
    --blue:#0255a3;
    --navy:#0f1f6e;
    --white:#ffffff;
    --stage:#e9e9ec;
  }
  *{box-sizing:border-box;margin:0;padding:0}
  html,body{width:1200px;height:900px;overflow:hidden;background:var(--stage)}
  body{font-family:"Josefin Sans",sans-serif;position:relative}
  .page{position:absolute;width:560px;height:400px;overflow:hidden;box-shadow:0 6px 18px rgba(0,0,0,.18)}
  .page svg{display:block}
  .cover{left:320px;top:30px;background:var(--navy)}
  .feature{left:30px;top:465px}
  .details{left:610px;top:465px;background:var(--blue);color:var(--white);text-align:center;padding:56px 48px 0}
  .details__title{color:var(--pink);font-weight:400;font-size:22px;letter-spacing:2px;margin-bottom:14px}
  .details__copy{font-size:12.5px;line-height:1.45;letter-spacing:1.2px;text-transform:uppercase;font-weight:300}
  .details__band{display:inline-block;margin:16px 0 18px;background:var(--pink);padding:6px 12px 4px;font-size:14px;letter-spacing:1.6px;text-transform:uppercase}
  .scents{list-style:none;font-size:12.5px;line-height:1.5;letter-spacing:1.4px;text-transform:uppercase;font-weight:300}
  .brand-name{font-family:"Josefin Sans",sans-serif;font-weight:600;font-size:20px;fill:var(--violet)}
  .price-label{font-family:"Josefin Sans",sans-serif;fill:var(--white);font-weight:400}
</style>
</head>
<body>

<section class="page cover" aria-label="Catalog cover">
  <svg width="560" height="400" viewBox="0 0 560 400">
    <defs>
      <polygon id="hex" points="96,0 48,83 -48,83 -96,0 -48,-83 48,-83"/>
      <linearGradient id="marble-tone" x1="0" y1="0" x2="1" y2="1">
        <stop offset="0" stop-color="#3b3f9e"/>
        <stop offset="1" stop-color="#7b6fb8"/>
      </linearGradient>
      <linearGradient id="pink-tone" x1="0" y1="0" x2="0" y2="1">
        <stop offset="0" stop-color="#ee6fb0"/>
        <stop offset="1" stop-color="#d8378a"/>
      </linearGradient>
    </defs>
    <rect width="560" height="400" fill="var(--navy)"/>
    <g stroke="#ffffff" stroke-width="4">
      <g role="img" aria-label="Photo of pastel bath bombs on cones"><use href="#hex" x="280" y="27" fill="#f0dde6"/></g>
      <g role="img" aria-label="Photo of a bath bomb"><use href="#hex" x="280" y="373" fill="#e9b8cf"/></g>
      <g role="img" aria-label="Photo of a gift pail of bath products"><use href="#hex" x="130" y="113.5" fill="url(#pink-tone)"/></g>
      <g role="img" aria-label="Photo of pastel bath bombs"><use href="#hex" x="130" y="286.5" fill="#e58fbd"/></g>
      <g role="img" aria-label="Photo of a cupcake bath bomb"><use href="#hex" x="430" y="113.5" fill="url(#pink-tone)"/></g>
      <g role="img" aria-label="Photo of lip balm jars"><use href="#hex" x="430" y="286.5" fill="#e2559f"/></g>
      <g role="img" aria-label="Marbled texture"><use href="#hex" x="-20" y="27" fill="url(#marble-tone)"/></g>
      <g role="img" aria-label="Marbled texture"><use href="#hex" x="-20" y="200" fill="url(#marble-tone)"/></g>
      <g role="img" aria-label="Marbled texture"><use href="#hex" x="-20" y="373" fill="url(#marble-tone)"/></g>
      <g role="img" aria-label="Marbled texture"><use href="#hex" x="580" y="27" fill="url(#marble-tone)"/></g>
      <g role="img" aria-label="Photo of a pink product bottle"><use href="#hex" x="580" y="200" fill="#df4c99"/></g>
      <g role="img" aria-label="Marbled texture"><use href="#hex" x="580" y="373" fill="url(#marble-tone)"/></g>
    </g>
    <use href="#hex" x="280" y="200" fill="var(--pink)" stroke="#ffffff" stroke-width="4"/>
    <polygon points="358,200 319,268 241,268 202,200 241,132 319,132" fill="#f4f1f7" stroke="#ffffff" stroke-width="3"/>
    <circle cx="280" cy="180" r="8" fill="var(--violet)"/>
    <text class="brand-name" x="280" y="214" text-anchor="middle">Tessa Moor</text>
  </svg>
</section>

<section class="page feature" aria-label="Bodywash feature page">
  <svg width="560" height="400" viewBox="0 0 560 400">
    <defs>
      <linearGradient id="marble-bg" x1="0" y1="0" x2="1" y2="1">
        <stop offset="0" stop-color="#3f4fa6"/>
        <stop offset=".35" stop-color="#2f7a78"/>
        <stop offset=".6" stop-color="#8a7a5a"/>
        <stop offset="1" stop-color="#6e5aa8"/>
      </linearGradient>
      <linearGradient id="product-tone" x1="0" y1="0" x2="1" y2="1">
        <stop offset="0" stop-color="#6a66d6"/>
        <stop offset=".55" stop-color="#c9b8e6"/>
        <stop offset="1" stop-color="#f4eedc"/>
      </linearGradient>
    </defs>
    <rect width="560" height="400" fill="url(#marble-bg)" role="img" aria-label="Marbled teal, purple and gold background"/>
    <polygon points="250,170 195,265 85,265 30,170 85,75 195,75" fill="var(--violet)" stroke="#ffffff" stroke-width="4"/>
    <polygon points="500,200 425,330 275,330 200,200 275,70 425,70" fill="url(#product-tone)" stroke="#ffffff" stroke-width="8" role="img" aria-label="Photo of a bodywash bottle beside a bath sponge"/>
    <text class="price-label" x="128" y="158" text-anchor="middle" font-size="21" letter-spacing="2">BODYWASH</text>
    <text class="price-label" x="128" y="192" text-anchor="middle" font-size="27" letter-spacing="2">$8.00</text>
    <polygon points="250,300 228,338 184,338 162,300 184,262 228,262" fill="var(--pink)" stroke="#ffffff" stroke-width="4"/>
  </svg>
</section>

<section class="page details" aria-label="Bodywash details page">
  <h2 class="details__title">BODYWASH</h2>
  <p class="details__copy">A great accompaniment to the body lotion. Our new body wash is a wonderful addition to your tub or shower. The gentle lather removes impurities, feels great on the skin and leaves it soft and smooth</p>
  <p class="details__band">Available in 5 delightfully scented varieties</p>
  <ul class="scents">
    <li>Lemon</li>
    <li>Lavender</li>
    <li>Rosemary</li>
    <li>Grapefruit</li>
    <li>Mango</li>
  </ul>
</section>

</body>
</html>
```